Calm Fern Wellcare- Aged Care and Community Services

Looking for brochure to advertise our services. I will attach a draft that we do not want to use. Looking for graphics that are as natural as possible to present a personalised service. We supply services to aged people and people with disability. Please make it look classy and professional at the same time. I am looking for creativity. I have also attached the logo. Site addresses can be the last page. ideally looking for 2 designs, one A4 and another smaller possibly DL. Looking for creative out of the box thinkers. Thank you.

Target Market(s)

Aged Care service providers, disability service providers and private hospitals

Font styles to use
Serif
Sans Serif
Script

Colors
6b449b
886aae
eea4c8
f59195
fac994
3176b5
0555a3
cedeed
e4daeb

Requirements
Must have
• Targeted imagery, content and contact details
Nice to have
• personal profiles of people happy with our services

```html
<!DOCTYPE html>
<html lang="en">
<head>
<meta charset="utf-8">
<title>Calm Fern Wellcare – Our Vision Flyer</title>
<link href="https://fonts.googleapis.com/css2?family=PT+Sans:wght@400;700&display=swap" rel="stylesheet">
<style>
  :root {
    --page-bg: #e9eef2;
    --paper: #ffffff;
    --pink: #ec1f7f;
    --purple: #6b3fa0;
    --text-purple: #6b449b;
    --photo-light: #f6ead2;
    --photo-warm: #d9b77e;
    --photo-green: #7f8f4e;
    --photo-blue: #3a6fb3;
  }
  * { box-sizing: border-box; margin: 0; padding: 0; }
  html, body {
    width: 1200px;
    height: 1200px;
    overflow: hidden;
    background: var(--page-bg);
    font-family: "PT Sans", "Helvetica Neue", Arial, sans-serif;
  }
  .flyer {
    position: absolute;
    left: 190px;
    top: 70px;
    width: 820px;
    height: 1060px;
    background: var(--paper);
    overflow: hidden;
    box-shadow: 0 18px 40px rgba(40, 60, 80, 0.18);
  }
  .hero-photo {
    position: absolute;
    left: 0;
    top: 0;
    width: 820px;
    height: 700px;
    background:
      radial-gradient(ellipse 45% 40% at 18% 18%, var(--photo-light) 0%, rgba(246,234,210,0) 70%),
      radial-gradient(ellipse 40% 45% at 70% 35%, var(--photo-blue) 0%, rgba(58,111,179,0) 70%),
      linear-gradient(160deg, #efe3c6 0%, var(--photo-warm) 40%, var(--photo-green) 100%);
  }
  .wave {
    position: absolute;
    left: 0;
    top: 0;
    width: 820px;
    height: 1060px;
  }
  .brand {
    position: absolute;
    left: 26px;
    top: 620px;
    width: 280px;
    text-align: center;
    color: var(--text-purple);
  }
  .brand-mark {
    width: 26px;
    height: 26px;
    border-radius: 50%;
    background: var(--pink);
    margin: 0 auto 14px;
  }
  .brand-name {
    font-size: 34px;
    font-weight: 400;
    line-height: 1.15;
    color: var(--text-purple);
  }
  .contact {
    position: absolute;
    left: 26px;
    top: 796px;
    width: 280px;
    text-align: center;
    color: var(--text-purple);
    font-size: 17px;
    line-height: 23px;
  }
  .contact-icon {
    display: block;
    width: 30px;
    height: 30px;
    margin: 0 auto 6px;
  }
  .contact-address { margin-bottom: 12px; }
  .vision {
    position: absolute;
    left: 340px;
    top: 740px;
    width: 430px;
    text-align: center;
  }
  .vision-title {
    font-size: 72px;
    font-weight: 400;
    color: var(--pink);
    line-height: 1;
    margin-bottom: 22px;
  }
  .vision-text {
    font-size: 20px;
    line-height: 27px;
    text-transform: uppercase;
    color: var(--text-purple);
  }
</style>
</head>
<body>
  <main class="flyer">
    <div class="hero-photo" role="img" aria-label="Photo of a smiling older woman seated outdoors, embraced from behind by a smiling carer in a blue uniform, in warm sunlight"></div>

    <svg class="wave" viewBox="0 0 820 1060" aria-hidden="true">
      <path fill="var(--purple)" d="M0,282 C210,245 400,300 545,440 C640,535 740,575 820,585 L820,610 C740,600 640,560 545,465 C400,325 210,270 0,307 Z"/>
      <path fill="var(--pink)" d="M0,305 C210,268 400,323 545,463 C640,558 740,598 820,608 L820,700 C720,705 600,665 520,600 C380,480 220,410 0,445 Z"/>
      <path fill="var(--paper)" d="M150,425 C300,405 420,470 540,570 C610,625 690,655 760,665 C660,650 590,620 520,560 C410,470 290,420 150,425 Z"/>
      <path fill="var(--purple)" d="M560,630 C640,672 730,690 820,680 L820,700 C720,705 630,680 560,630 Z"/>
      <path fill="var(--paper)" d="M0,445 C220,410 380,480 520,600 C600,665 720,705 820,700 L820,1060 L0,1060 Z"/>
    </svg>

    <div class="brand">
      <div class="brand-mark"></div>
      <p class="brand-name">Calm Fern Wellcare</p>
    </div>

    <address class="contact" style="font-style: normal;">
      <svg class="contact-icon" viewBox="0 0 30 30" aria-hidden="true">
        <circle cx="15" cy="15" r="14" fill="var(--text-purple)"/>
        <path fill="#fff" d="M15,6 C11.1,6 8.5,8.8 8.5,12.3 C8.5,16.7 15,24 15,24 C15,24 21.5,16.7 21.5,12.3 C21.5,8.8 18.9,6 15,6 Z"/>
        <circle cx="15" cy="12.3" r="2.6" fill="var(--text-purple)"/>
      </svg>
      <p class="contact-address">18 Banksia Road Oakvale<br>WA 6120 Australia<br>Ground Floor, 47 Marlow<br>Street Eastbrook<br>SA 5080 Australia</p>
      <svg class="contact-icon" viewBox="0 0 30 30" aria-hidden="true">
        <circle cx="15" cy="15" r="14" fill="var(--text-purple)"/>
        <path fill="#fff" d="M8,11 C8,9 10,8 15,8 C20,8 22,9 22,11 L22,12.5 L19,12.5 L19,11 L11,11 L11,12.5 L8,12.5 Z"/>
        <rect x="9" y="13.5" width="12" height="8" rx="1.5" fill="#fff"/>
        <circle cx="15" cy="17.5" r="2" fill="var(--text-purple)"/>
      </svg>
      <p class="contact-phone">(08) 95550142</p>
    </address>

    <section class="vision">
      <h1 class="vision-title">Our Vision</h1>
      <p class="vision-text">Our vision is to be most responsive staffing solutions provider in WA, whilst sourcing and placing staff hold strong values which includes ethics, accountiblity, respect, integirity and adaptablity</p>
    </section>
  </main>
</body>
</html>
```